Looking for awesome business card design with attached existing logo

We are a water, mold, and fire damage restoration company called "Torvane Seco" Looking for an awesome business card that is edgy yet professional and unique. Show me what you got!

```html
<!DOCTYPE html>
<html lang="en">
<head>
<meta charset="utf-8">
<title>Torvane Seco — Business Card</title>
<link href="https://fonts.googleapis.com/css2?family=Open+Sans:wght@400;600;700&display=swap" rel="stylesheet">
<style>
  :root {
    --stage: #000000;
    --gold: #d3972e;
    --teal: #2f4b55;
    --ink: #161616;
    --paper: #ffffff;
    --cream: #f7efdd;
  }
  * { margin: 0; padding: 0; box-sizing: border-box; }
  html, body {
    width: 1200px; height: 1200px; overflow: hidden;
    background: var(--stage);
    font-family: "Open Sans", Arial, sans-serif;
  }
  .canvas { position: relative; width: 1200px; height: 1200px; }

  .card {
    position: absolute;
    left: 218px;
    width: 756px;
    height: 431px;
    overflow: hidden;
  }
  .card--front { top: 142px; background: var(--gold); }
  .card--back  { top: 619px; background: var(--paper); }

  /* Front */
  .front-name {
    position: absolute; inset: 0;
    display: flex; align-items: center; justify-content: center;
    color: var(--paper);
    font-weight: 700;
    font-size: 58px;
    letter-spacing: 1px;
  }

  /* Back */
  .brand-name {
    position: absolute; left: 26px; top: 78px;
    color: var(--teal);
    font-weight: 700;
    font-size: 31px;
    letter-spacing: 0.5px;
  }
  .address {
    position: absolute; left: 26px; top: 204px;
    color: var(--ink);
    font-size: 19px;
    line-height: 27px;
  }
  .contacts {
    position: absolute; left: 26px; top: 327px;
    list-style: none;
    color: var(--ink);
    font-size: 19px;
    line-height: 27px;
  }
  .contacts li { display: flex; align-items: center; gap: 12px; }
  .contacts svg { width: 18px; height: 18px; fill: none; stroke: var(--gold); stroke-width: 2; }

  .deco-ring {
    position: absolute; left: 490px; top: 67px;
    width: 224px; height: 224px;
    border: 22px solid var(--cream);
    border-radius: 50%;
  }
  .person {
    position: absolute; right: 29px; top: 206px;
    text-align: right;
  }
  .person-name {
    font-weight: 700; font-size: 31px; line-height: 38px;
    color: var(--teal);
  }
  .person-name .first { color: var(--gold); }
  .person-title {
    font-size: 21px; line-height: 30px; color: var(--ink);
  }
  .accent-bar {
    position: absolute; right: 0; top: 211px;
    width: 22px; height: 67px;
    background: var(--gold);
  }
</style>
</head>
<body>
<main class="canvas">
  <section class="card card--front">
    <div class="front-name">Torvane Seco</div>
  </section>

  <section class="card card--back">
    <div class="deco-ring" aria-hidden="true"></div>
    <div class="brand-name">Torvane Seco</div>
    <p class="address">418 Linden Hollow Rd. Suite 12<br>Alder Springs, TX 75990</p>
    <ul class="contacts">
      <li>
        <svg viewBox="0 0 24 24"><path d="M5 3h4l2 5-2.5 1.5a11 11 0 0 0 6 6L16 13l5 2v4a2 2 0 0 1-2 2A17 17 0 0 1 3 5a2 2 0 0 1 2-2z"/></svg>
        <span>(555) 204-7316</span>
      </li>
      <li>
        <svg viewBox="0 0 24 24"><rect x="3" y="6" width="18" height="13" rx="1"/><path d="M3 7l9 7 9-7"/></svg>
        <span>info@website.com</span>
      </li>
      <li>
        <svg viewBox="0 0 24 24"><circle cx="12" cy="12" r="9"/><path d="M3 12h18M12 3c3 3 3 15 0 18M12 3c-3 3-3 15 0 18"/></svg>
        <span>www.website.com</span>
      </li>
    </ul>
    <div class="person">
      <div class="person-name"><span class="first">Mirela</span> Kovanda</div>
      <div class="person-title">Managing Director</div>
    </div>
    <div class="accent-bar"></div>
  </section>
</main>
</body>
</html>
```